Develop website for Cloud Security Startup

Looking for a logo that conveys the outsourced security and management of clients data, systems and development in Azure, Aws and Google with an emphasis on security and compliance

Target Market(s)

Companies looking for professional services IT firm

Coding

Coded - Design and coding required

Number of Pages Required

5+ page

Font styles to use
Sans Serif

Colors
0455a3
33a6d7

Requirements
Must have
• Landing Page
- Help me get started

Move to the cloud safely
- Benefits of Cloud

What we do
- Cloud Adoption
- Managed Services
- Optimise

Resources
- News
- Resources
- Events
- Webinars
- Not for profit
- Case Studies
- Support Button
- Incident Button

Company
- About Us
- Why Vorbelix?
- Acreditations
- Quindor Skyvault Partner
- Net Promoter Score
- Careers
- Contact Us

Contact Us

```html
<!DOCTYPE html>
<html lang="en">
<head>
<meta charset="utf-8">
<title>Vorbelix — Effective Technology Management</title>
<link rel="stylesheet" href="https://fonts.googleapis.com/css2?family=Jost:wght@400;500;600&display=swap">
<style>
:root{
  --brand:#0455a3;
  --accent:#33a6d7;
  --navy:#1d3f6e;
  --pale:#eef3f9;
  --ink:#2b2b2b;
  --footer:#333333;
  --white:#ffffff;
}
*{margin:0;padding:0;box-sizing:border-box}
html,body{width:1200px;height:4274px;overflow:hidden}
body{position:relative;background:var(--white);font-family:"Jost",sans-serif;color:var(--ink)}
.abs{position:absolute}
svg.bg{position:absolute;left:0;top:0}

/* hero */
.hero-art{left:498px;top:116px;width:702px;height:560px;border-radius:40px;
  background:radial-gradient(ellipse at 55% 45%,rgba(255,60,90,.35),rgba(20,110,170,.25) 45%,rgba(10,60,120,0) 72%)}
.brand-top{left:171px;top:108px;display:flex;align-items:center;gap:12px;color:var(--brand);font-weight:600;font-size:34px;letter-spacing:2px}
.brand-top .dot{width:26px;height:26px;border-radius:50%;background:var(--brand)}
.nav{left:536px;top:55px;display:flex;gap:30px}
.nav a{color:var(--white);text-decoration:none;font-size:15px;font-weight:500}
.hero-title{left:171px;top:285px;color:var(--white);font-size:62px;font-weight:500;letter-spacing:3px}
.hero-sub{left:171px;top:386px;color:var(--white);font-size:33px;font-weight:500}
.btn{display:inline-flex;align-items:center;justify-content:center;border-radius:28px;color:var(--white);font-weight:500;font-size:18px;text-decoration:none}
.hero-btn{left:173px;top:473px;width:136px;height:62px;background:var(--accent)}

/* headings */
.section-title{position:absolute;left:0;width:1200px;text-align:center;color:var(--brand);font-size:36px;font-weight:500}
.section-title span{position:relative;display:inline-block}
.tick{position:absolute;right:-34px;bottom:-12px;width:48px;height:40px}

/* services */
.service{position:absolute;top:1067px;width:246px;height:344px;text-align:center}
.service svg.drop{position:absolute;left:0;top:0}
.service .icon{position:absolute;left:93px;top:60px;width:60px;height:60px}
.service h3{position:absolute;top:150px;left:-20px;width:286px;color:var(--brand);font-size:21px;font-weight:500}
.service p{position:absolute;top:193px;left:-20px;width:286px;font-size:13px;line-height:22px;color:#444}

/* about */
.col{position:absolute;top:1727px;width:410px}
.col .ico{width:66px;height:62px}
.col h2{margin-top:42px;font-size:36px;font-weight:500;position:relative;display:inline-block}
.col p{margin-top:34px;font-size:13px;line-height:27px}
.col .btn{margin-top:42px;width:121px;height:53px;font-size:17px}
.about{left:173px;color:var(--brand)}
.about p{color:#333}
.about .btn{background:var(--brand)}
.why{left:629px;color:var(--white)}
.why .btn{background:var(--accent)}

/* resources */
.card{position:absolute;top:2593px;width:264px;height:432px;border:2px solid #333;text-align:center;background:var(--white)}
.card .photo{height:204px;background:linear-gradient(135deg,#1c3a5e,#4c7fae 55%,#0e2444)}
.card .date{position:absolute;left:69px;top:179px;width:123px;height:50px;line-height:50px;background:var(--brand);color:var(--white);font-size:15px}
.card .date.light{background:var(--accent)}
.card h3{margin-top:48px;font-size:20px;font-weight:500;color:#111}
.card p{margin:10px auto 0;width:236px;font-size:12.5px;line-height:20px;color:#333}
.card .more{display:inline-block;margin-top:16px;width:88px;height:40px;line-height:38px;border:2px solid #333;font-size:12px;color:#333}

/* contact */
.contact-mark{left:173px;top:3146px;width:422px;height:415px;display:flex;flex-direction:column;align-items:center;justify-content:center;gap:24px}
.contact-mark .disc{width:250px;height:250px;border-radius:50%;background:linear-gradient(135deg,#0a3f8f,#2d8fdc)}
.contact-mark .name{font-size:44px;font-weight:600;color:var(--brand);letter-spacing:3px}
.contact-title{left:646px;top:3155px;color:var(--brand);font-size:36px;font-weight:500}
.field{position:absolute;border:2px solid #333;font-size:15px;padding:14px 0 0 12px;color:#333}
.submit{left:646px;top:3489px;width:129px;height:53px;background:var(--brand);color:var(--white);font-size:18px;font-weight:500;display:flex;align-items:center;justify-content:center}

/* footer */
.foot-brand{left:173px;top:3930px;display:flex;align-items:center;gap:14px;color:var(--white);font-size:46px;font-weight:500;letter-spacing:3px}
.foot-brand .dot{width:34px;height:34px;border-radius:50%;background:var(--white)}
.foot-tag{left:173px;top:3998px;color:var(--white);font-size:14px;letter-spacing:.5px}
.foot-head{color:var(--white);font-size:19px;font-weight:500;top:3872px}
.foot-links{left:546px;top:3914px;list-style:none}
.foot-links li{color:var(--white);font-size:15px;height:40.5px}
.contact-item{position:absolute;left:765px;display:flex;gap:12px;color:var(--white)}
.contact-item .circ{width:46px;height:46px;border-radius:50%;background:var(--white);display:flex;align-items:center;justify-content:center;flex-shrink:0}
.contact-item small{display:block;font-size:12px}
.contact-item b{display:block;font-size:19px;font-weight:500;line-height:26px}
.rule{left:173px;top:4198px;width:855px;height:2px;background:#bbb}
.copy{left:0;top:4228px;width:1200px;text-align:center;color:var(--white);font-size:13px}
</style>
</head>
<body>

<!-- hero background -->
<svg class="bg" width="1200" height="880" viewBox="0 0 1200 880" aria-hidden="true">
  <defs>
    <linearGradient id="heroGrad" x1="0" y1="0" x2="0.6" y2="1">
      <stop offset="0" stop-color="#36e0ea"/>
      <stop offset="0.45" stop-color="#0d8ab0"/>
      <stop offset="1" stop-color="#0b3c78"/>
    </linearGradient>
  </defs>
  <polygon points="0,0 1200,0 1200,660 196,815 0,680" fill="url(#heroGrad)"/>
  <path d="M0,0 H400 C430,90 380,220 250,230 C150,238 60,260 0,265 Z" fill="#5ff0f2" opacity=".55"/>
  <polygon points="8,700 196,826 1188,690 1188,722 196,866 8,736" fill="var(--brand)"/>
</svg>
<div class="abs hero-art" role="img" aria-label="Illustration of cloud servers, laptop and security circuitry"></div>
<div class="abs brand-top"><span class="dot"></span>VORBELIX</div>
<nav class="abs nav"><a>HOME</a><a>WHAT WE DO</a><a>RESOURCES</a><a>COMPANY</a><a>CONTACT US</a></nav>
<h1 class="abs hero-title">VORBELIX</h1>
<p class="abs hero-sub">HELP ME GET STARTED</p>
<a class="abs btn hero-btn">READ MORE</a>

<!-- what we do -->
<h2 class="section-title" style="top:940px"><span>WHAT WE DO<svg class="tick" viewBox="0 0 48 40"><path d="M4 22 L18 34 L44 6" fill="none" stroke="var(--accent)" stroke-width="8"/></svg></span></h2>

<div class="service" style="left:173px">
  <svg class="drop" width="246" height="344" viewBox="0 0 246 344"><path d="M123 0 A123 123 0 0 1 230 180 L123 344 L16 180 A123 123 0 0 1 123 0Z" fill="var(--pale)"/></svg>
  <svg class="icon" viewBox="0 0 60 60" fill="none" stroke="var(--brand)" stroke-width="3"><path d="M14 44 A12 12 0 0 1 14 20 A16 16 0 0 1 44 18 A13 13 0 0 1 46 44"/><path d="M30 24 L42 30 L42 44 L30 50 L18 44 L18 30 Z M18 30 L30 36 L42 30 M30 36 V50"/></svg>
  <h3>CLOUD ADOPTION</h3>
  <p>Nemo enim ipsam voluptatem quia volup tas sit aspernatur aut odit aut fugit, sed quia dolores</p>
</div>
<div class="service" style="left:477px">
  <svg class="drop" width="246" height="344" viewBox="0 0 246 344"><path d="M123 344 A123 123 0 0 1 16 164 L123 0 L230 164 A123 123 0 0 1 123 344Z" fill="var(--pale)"/></svg>
  <svg class="icon" viewBox="0 0 60 60" fill="none" stroke="var(--brand)" stroke-width="3"><path d="M30 6 L50 14 V30 C50 42 40 50 30 54 C20 50 10 42 10 30 V14 Z"/><circle cx="30" cy="31" r="11"/><path d="M24 31 L29 36 L37 27"/></svg>
  <h3>MANAGED SERVICES</h3>
  <p>Nemo enim ipsam voluptatem quia volup tas sit aspernatur aut odit aut fugit, sed quia dolores</p>
</div>
<div class="service" style="left:774px">
  <svg class="drop" width="246" height="344" viewBox="0 0 246 344"><path d="M123 0 A123 123 0 0 1 230 180 L123 344 L16 180 A123 123 0 0 1 123 0Z" fill="var(--pale)"/></svg>
  <svg class="icon" viewBox="0 0 60 60" fill="none" stroke="var(--ink)" stroke-width="3"><path d="M16 44 A12 12 0 0 1 14 20 A16 16 0 0 1 44 18 A13 13 0 0 1 46 44"/><path d="M30 26 V52 M21 43 L30 52 L39 43" stroke="var(--brand)"/></svg>
  <h3>OPTIMISE</h3>
  <p>Nemo enim ipsam voluptatem quia volup tas sit aspernatur aut odit aut fugit, sed quia dolores</p>
</div>

<!-- about / why -->
<svg class="bg" width="1200" height="4274" viewBox="0 0 1200 4274" aria-hidden="true" style="pointer-events:none">
  <polygon points="0,1665 1000,1558 1200,1665 1200,2240 220,2320 0,2262" fill="var(--pale)"/>
  <polygon points="601,1600 1000,1558 1200,1665 1200,2240 601,2290" fill="var(--navy)"/>
  <polygon points="8,1637 1000,1530 1195,1628 1195,1660 1000,1562 8,1652" fill="var(--brand)"/>
  <polygon points="8,2250 220,2336 1190,2245 1190,2265 220,2358 8,2272" fill="var(--brand)"/>
  <polygon points="0,3815 1000,3710 1200,3815 1200,4274 0,4274" fill="var(--footer)"/>
  <polygon points="10,3770 1000,3665 1195,3765 1195,3800 1000,3702 10,3800" fill="var(--brand)"/>
</svg>

<div class="col about">
  <svg class="ico" viewBox="0 0 66 62" fill="none" stroke="var(--accent)" stroke-width="2.5"><rect x="2" y="2" width="62" height="16"/><path d="M8 10h4M16 10h4M24 10h4"/><path d="M2 24h62M2 34h10M54 34h10M2 24v18h10M64 24v18H54"/><path d="M33 22 L48 28 V40 C48 50 40 56 33 60 C26 56 18 50 18 40 V28 Z" stroke="var(--brand)"/><path d="M26 41 L31 46 L40 36" stroke="var(--brand)"/></svg><br>
  <h2>ABOUT US<svg class="tick" viewBox="0 0 48 40"><path d="M4 22 L18 34 L44 6" fill="none" stroke="var(--accent)" stroke-width="8"/></svg></h2>
  <p>Nemo enim ipsam voluptatem quia voluptas sit aspernatur aut odit aut fugit, sed quia consequuntur magni dolores eos qui ratione vo luptatem sequi nesciunt. Neque porro quisquam est, qui dolorem ipsum quia dolor sit amet, consectetur, adipisci velit, sed quia non numquam eius modi tempora incidunt ut labore et dolore magnam aliquam quaerat voluptatem.</p>
  <a class="btn">READ MORE</a>
</div>
<div class="col why">
  <svg class="ico" viewBox="0 0 66 62" fill="none" stroke="var(--white)" stroke-width="2.5"><path d="M16 40 A12 12 0 0 1 14 16 A17 17 0 0 1 46 14 A13 13 0 0 1 50 40 Z"/><path d="M33 40 V50 M18 50 H48"/><rect x="28" y="46" width="10" height="8"/></svg><br>
  <h2>WHY VORBELIX?<svg class="tick" viewBox="0 0 48 40"><path d="M4 22 L18 34 L44 6" fill="none" stroke="var(--white)" stroke-width="8"/></svg></h2>
  <p>Nemo enim ipsam voluptatem quia voluptas sit aspernatur aut odit aut fugit, sed quia consequuntur magni dolores eos qui ratione vo luptatem sequi nesciunt. Neque porro quisquam est, qui dolorem ipsum quia dolor sit amet, consectetur, adipisci velit, sed quia non numquam eius modi tempora incidunt ut labore et dolore magnam aliquam quaerat voluptatem.</p>
  <a class="btn">READ MORE</a>
</div>

<!-- resources -->
<h2 class="section-title" style="top:2462px"><span>OUR RESOURCES<svg class="tick" viewBox="0 0 48 40"><path d="M4 22 L18 34 L44 6" fill="none" stroke="var(--accent)" stroke-width="8"/></svg></span></h2>

<article class="card" style="left:173px">
  <div class="photo" role="img" aria-label="Two engineers talking in a server room"></div>
  <div class="date">JAN 20, 2021</div>
  <h3>LATEST NEWS</h3>
  <p>Lorem ipsum dolor sit amet, consecte tur adipiscing elit, sed do eiusmod tempor labore.</p>
  <span class="more">READ MORE</span>
</article>
<article class="card" style="left:468px">
  <div class="photo" role="img" aria-label="Hands typing on a laptop with cloud network icons" style="background:linear-gradient(135deg,#2a5b8a,#9cc4e0 60%,#e7eef4)"></div>
  <div class="date light">MAY 05, 2021</div>
  <h3>WEBINARS</h3>
  <p>Lorem ipsum dolor sit amet, consecte tur adipiscing elit, sed do eiusmod tempor labore.</p>
  <span class="more">READ MORE</span>
</article>
<article class="card" style="left:764px">
  <div class="photo" role="img" aria-label="Team working at monitors in an operations centre" style="background:linear-gradient(135deg,#0d2038,#3a6e9a 55%,#142c48)"></div>
  <div class="date">JUN 12, 2021</div>
  <h3>CASE STUDIES</h3>
  <p>Lorem ipsum dolor sit amet, consecte tur adipiscing elit, sed do eiusmod tempor labore.</p>
  <span class="more">READ MORE</span>
</article>

<!-- contact -->
<div class="abs contact-mark"><span class="disc"></span><span class="name">VORBELIX</span></div>
<h2 class="abs contact-title" style="position:absolute">CONTACT US<svg class="tick" viewBox="0 0 48 40" style="right:-40px"><path d="M4 22 L18 34 L44 6" fill="none" stroke="var(--accent)" stroke-width="8"/></svg></h2>
<div class="field" style="left:646px;top:3257px;width:186px;height:53px">Name</div>
<div class="field" style="left:845px;top:3257px;width:183px;height:53px">Phone</div>
<div class="field" style="left:646px;top:3325px;width:382px;height:53px">Email</div>
<div class="field" style="left:646px;top:3391px;width:382px;height:80px">Message</div>
<div class="abs submit">SUBMIT</div>

<!-- footer -->
<div class="abs foot-brand"><span class="dot"></span>VORBELIX</div>
<div class="abs foot-tag">EFFECTIVE TECHNOLOGY MANAGEMENT</div>
<div class="abs foot-head" style="left:546px">QUICK LINKS</div>
<ul class="abs foot-links"><li>HOME</li><li>WHAT WE DO</li><li>RESOURCES</li><li>COMPANY</li><li>CONTACT US</li></ul>
<div class="abs foot-head" style="left:765px">CONTACT US</div>
<div class="contact-item" style="top:3920px">
  <span class="circ"><svg width="24" height="24" viewBox="0 0 24 24" fill="none" stroke="#333" stroke-width="1.8"><path d="M5 3h4l2 5-2.5 1.5a11 11 0 0 0 6 6L16 13l5 2v4a2 2 0 0 1-2 2A17 17 0 0 1 3 5a2 2 0 0 1 2-2z"/></svg></span>
  <div><small>CALL:</small><b>123 456 7890</b></div>
</div>
<div class="contact-item" style="top:3995px">
  <span class="circ"><svg width="24" height="24" viewBox="0 0 24 24" fill="none" stroke="#333" stroke-width="1.8"><rect x="3" y="5" width="18" height="14"/><path d="M3 5l9 8 9-8"/></svg></span>
  <div><small>MAIL:</small><b>info@vorbelix-mail.com</b></div>
</div>
<div class="contact-item" style="top:4062px">
  <span class="circ"><svg width="24" height="24" viewBox="0 0 24 24" fill="none" stroke="#333" stroke-width="1.8"><path d="M12 22s7-7 7-12a7 7 0 0 0-14 0c0 5 7 12 7 12z"/><circle cx="12" cy="10" r="2.5"/></svg></span>
  <div><small>ADDRESS:</small><b>Dummy Street, City,<br>12345</b></div>
</div>
<div class="abs rule"></div>
<p class="abs copy">COPYRIGHTS @ 2021 VORBELIX. ALL RIGHTS RESERVED.</p>

</body>
</html>
```